Bright Harbor Business Cards & Stationary
Bright Harbor
Bright Harbor Business Cards & Stationary -
Creative Brief
Professional
Dana Verick
4417 Wexmoor Lane Bozeman, MT 59263
dana@brightharborfunds.example
www.brightharborfunds.example
I have two companies, Bright Harbor Wealth Management, LLC and Bright Harbor Realty Advisors, LLC. I use the same logo for both companies with a different tagline and color for each company. I will use one business card for both companies with one company on one side of the card and the other company on the other side of the card. Other than the colors, the business cards and stationary will have the same design.
Bright Harbor Realty Advisors logo Dana Verick 4417 Wexmoor Lane Bozeman, MT 59263 406-739-4802 dana@brightharborestates.example www.brightharborestates.example

```html
<!DOCTYPE html>
<html lang="en">
<head>
<meta charset="utf-8">
<title>Bright Harbor Business Cards &amp; Stationary</title>
<link href="https://fonts.googleapis.com/css2?family=Libre+Baskerville:wght@700&family=Lato:wght@400;700&display=swap" rel="stylesheet">
<style>
:root{
  --backdrop:#8c8c8c;
  --paper:#ffffff;
  --wealth:#1f7f96;
  --realty:#5b4632;
  --ink:#233548;
  --muted:#7a8590;
  --mark-tint:#e8edf1;
  --caption:#d8d8d8;
}
*{box-sizing:border-box;margin:0;padding:0}
html,body{width:1200px;height:362px;overflow:hidden}
body{background:var(--backdrop);font-family:"Lato",sans-serif;position:relative}
.piece{position:absolute;background:var(--paper);box-shadow:0 1px 3px rgba(0,0,0,.35)}
.caption{position:absolute;font-size:5px;color:var(--caption);letter-spacing:.2px;white-space:nowrap}
.brand{display:flex;align-items:center;gap:3px}
.brand-square{background:var(--ink);flex:none}
.brand-name{font-family:"Libre Baskerville",serif;font-weight:700;color:var(--ink);line-height:1;text-transform:uppercase}
.tagline{font-size:3.4px;letter-spacing:.6px;color:var(--muted);text-transform:uppercase;margin-top:1px}
.contact{font-size:3.6px;line-height:1.45;color:var(--muted)}
/* business cards */
.card{width:96px;height:55px;left:20px;padding:6px}
.card .brand-square{width:8px;height:8px;background:var(--paper)}
.card .brand-name{font-size:7px;color:var(--paper)}
.card .tagline{color:#dfe9ec}
.card .contact{color:#eef3f4;margin-top:8px}
.card--wealth{top:178px;background:var(--wealth)}
.card--realty{top:246px;background:var(--realty)}
/* letterheads */
.letterhead{top:24px;width:238px;height:316px;padding:14px 18px;overflow:hidden}
.letterhead .band{position:absolute;left:0;right:0;height:9px}
.letterhead .band--top{top:0}
.letterhead .band--bottom{bottom:0}
.letterhead .brand-square{width:11px;height:11px}
.letterhead .brand-name{font-size:9px}
.letterhead .head-contact{position:absolute;right:16px;top:16px;text-align:right}
.letterhead .backdrop-mark{position:absolute;left:59px;top:100px;width:120px;height:104px;background:var(--mark-tint)}
.lh--wealth{left:140px}
.lh--wealth .band{background:var(--wealth)}
.lh--realty{left:396px}
.lh--realty .band{background:var(--realty)}
/* envelopes */
.envelope{width:226px;height:96px;left:640px;padding:8px 10px}
.envelope .brand-square{width:8px;height:8px}
.envelope .brand-name{font-size:6.5px}
.envelope .stripe{position:absolute;left:0;right:0;bottom:0;height:7px}
.env--wealth{top:60px}
.env--wealth .stripe{background:var(--wealth)}
.env--realty{top:196px}
.env--realty .stripe{background:var(--realty)}
.envelope-back{width:228px;height:92px;left:902px;overflow:hidden}
.envelope-back svg{position:absolute;inset:0}
.envelope-back .seal{position:absolute;left:108px;top:28px;width:12px;height:12px}
.back--wealth{top:62px}
.back--wealth .seal{background:var(--wealth)}
.back--realty{top:196px}
.back--realty .seal{background:var(--realty)}
</style>
</head>
<body>

<section class="piece card card--wealth" aria-label="Business card, wealth side">
  <div class="brand"><span class="brand-square"></span><span class="brand-name">Bright Harbor</span></div>
  <div class="tagline">Wealth Management</div>
  <div class="contact">Dana Verick · 406-739-4802<br>dana@brightharborfunds.example</div>
</section>
<div class="caption" style="left:20px;top:235px">Business Card Front</div>

<section class="piece card card--realty" aria-label="Business card, realty side">
  <div class="brand"><span class="brand-square"></span><span class="brand-name">Bright Harbor</span></div>
  <div class="tagline">Realty Advisors</div>
  <div class="contact">Dana Verick · 406-739-4802<br>dana@brightharborestates.example</div>
</section>
<div class="caption" style="left:20px;top:303px">Business Card Back</div>

<section class="piece letterhead lh--wealth" aria-label="Letterhead, wealth">
  <div class="band band--top"></div>
  <div class="brand"><span class="brand-square"></span><div><div class="brand-name">Bright Harbor</div><div class="tagline">Wealth Management</div></div></div>
  <div class="contact head-contact">4417 Wexmoor Lane<br>Bozeman, MT 59263<br>406-739-4802</div>
  <div class="backdrop-mark" role="img" aria-label="Faint brand mark area"></div>
  <div class="band band--bottom"></div>
</section>
<div class="caption" style="left:140px;top:343px">Letterhead Wealth</div>

<section class="piece letterhead lh--realty" aria-label="Letterhead, realty">
  <div class="band band--top"></div>
  <div class="brand"><span class="brand-square"></span><div><div class="brand-name">Bright Harbor</div><div class="tagline">Realty Advisors</div></div></div>
  <div class="contact head-contact">4417 Wexmoor Lane<br>Bozeman, MT 59263<br>406-739-4802</div>
  <div class="backdrop-mark" role="img" aria-label="Faint brand mark area"></div>
  <div class="band band--bottom"></div>
</section>
<div class="caption" style="left:396px;top:343px">Letterhead Realty</div>

<section class="piece envelope env--wealth" aria-label="Envelope front, wealth">
  <div class="brand"><span class="brand-square"></span><div><div class="brand-name">Bright Harbor</div><div class="tagline">Wealth Management</div></div></div>
  <div class="contact" style="margin-top:3px">4417 Wexmoor Lane<br>Bozeman, MT 59263</div>
  <div class="stripe"></div>
</section>
<div class="caption" style="left:640px;top:159px">Envelope Wealth</div>

<section class="piece envelope env--realty" aria-label="Envelope front, realty">
  <div class="brand"><span class="brand-square"></span><div><div class="brand-name">Bright Harbor</div><div class="tagline">Realty Advisors</div></div></div>
  <div class="contact" style="margin-top:3px">4417 Wexmoor Lane<br>Bozeman, MT 59263</div>
  <div class="stripe"></div>
</section>
<div class="caption" style="left:640px;top:295px">Envelope Realty</div>

<section class="piece envelope-back back--wealth" aria-label="Envelope back, wealth">
  <svg width="228" height="92" viewBox="0 0 228 92"><polyline points="0,0 114,40 228,0" fill="none" stroke="#d4d4d4" stroke-width="1"/></svg>
  <div class="seal"></div>
</section>
<div class="caption" style="left:902px;top:157px">Envelope Back</div>

<section class="piece envelope-back back--realty" aria-label="Envelope back, realty">
  <svg width="228" height="92" viewBox="0 0 228 92"><polyline points="0,0 114,40 228,0" fill="none" stroke="#d4d4d4" stroke-width="1"/></svg>
  <div class="seal"></div>
</section>
<div class="caption" style="left:902px;top:291px">Envelope Back</div>

</body>
</html>
```